Meridian Rest Supply Needs Business Card

Looking for a very nice looking business card. Creative but not extravagant. We sell beds and pillows across the U.S. and need something professional but catchy. I have attached the logo.

Name : Dale Fenwick
Title : President
Phone : (800) 417-2964
Email: sleep@quorvana.com
Website: www.quorvana.com

Can be single-sided or double-sided
horizontal or vertical

Can use Blues/Greys

Target Market(s)

Mass Market

Industry/Entity Type

Retail

Contact Information for Business Card

Name : Dale Fenwick
Title : President
Phone : (800) 417-2964
Email: sleep@quorvana.com
Website: www.quorvana.com

Requirements
Must have
• Clean, Modern, Smooth
• Can use Blues/Greys
• On the other side without the information - have something simple like www.quorvana.com or our logo
Nice to have
• Surprise me
Should not have
• Nothing crazy, nothing cluttered

```html
<!DOCTYPE html>
<html lang="en">
<head>
<meta charset="utf-8">
<title>Meridian Rest Supply – Business Card</title>
<link href="https://fonts.googleapis.com/css2?family=Montserrat:wght@300;400;500;700&display=swap" rel="stylesheet">
<style>
  :root {
    --stage: #e8e8e9;
    --card-grey: #58595b;
    --brand-blue: #29a8e0;
    --muted-blue: #4f8fb3;
    --ink-white: #ffffff;
    --rule: #d9d9d9;
  }
  * { margin: 0; padding: 0; box-sizing: border-box; }
  html, body { width: 1200px; height: 638px; overflow: hidden; }
  body {
    background: var(--stage);
    font-family: "Montserrat", Arial, sans-serif;
    display: flex;
    align-items: center;
    justify-content: center;
    gap: 70px;
  }
  .card {
    position: relative;
    width: 320px;
    height: 560px;
    background: var(--card-grey);
    overflow: hidden;
    box-shadow: 0 6px 18px rgba(0,0,0,.18);
  }
  .brand-name {
    position: absolute;
    left: 0; right: 0;
    text-align: center;
    font-family: "Montserrat", Arial, sans-serif;
    font-weight: 300;
    color: var(--brand-blue);
    letter-spacing: 1px;
  }
  .card-back .brand-name { top: 190px; font-size: 50px; }
  .card-front .brand-name { top: 40px; font-size: 50px; }

  .footer-bands { position: absolute; left: 0; bottom: 0; width: 320px; height: 60px; }

  .web-line {
    position: absolute;
    left: 52px; bottom: 92px;
    display: flex; align-items: center; gap: 10px;
    color: var(--ink-white);
    font-size: 17px;
    letter-spacing: .5px;
  }
  .icon { width: 20px; height: 20px; flex: none; }

  .accent-bar {
    position: absolute;
    left: 0; top: 208px;
    width: 128px; height: 46px;
    background: var(--brand-blue);
  }
  .name-plate {
    position: absolute;
    right: 0; top: 200px;
    width: 172px; height: 100px;
    background: var(--brand-blue);
    color: var(--ink-white);
    text-align: center;
    padding-top: 10px;
  }
  .name-plate .person {
    font-weight: 700;
    font-size: 26px;
    line-height: 26px;
  }
  .name-plate .title {
    display: flex; align-items: center; justify-content: center; gap: 6px;
    margin-top: 6px;
    font-size: 13px; font-weight: 400;
  }
  .name-plate .title::before,
  .name-plate .title::after {
    content: ""; width: 24px; height: 1px; background: var(--ink-white);
  }

  .contact-list {
    position: absolute;
    left: 24px; right: 24px; top: 350px;
    list-style: none;
  }
  .contact-list li {
    display: flex; align-items: center; gap: 10px;
    padding: 8px 0 8px 30px;
    color: var(--ink-white);
    font-size: 17px;
    letter-spacing: .5px;
  }
  .contact-list li + li { border-top: 1px solid var(--rule); }
</style>
</head>
<body>

  <section class="card card-back">
    <div class="brand-name">quorvana</div>
    <div class="web-line">
      <svg class="icon" viewBox="0 0 20 20" aria-hidden="true">
        <rect width="20" height="20" rx="4" fill="#29a8e0"/>
        <circle cx="10" cy="10" r="6" fill="none" stroke="#fff" stroke-width="1.3"/>
        <ellipse cx="10" cy="10" rx="2.6" ry="6" fill="none" stroke="#fff" stroke-width="1.1"/>
        <line x1="4" y1="10" x2="16" y2="10" stroke="#fff" stroke-width="1.1"/>
      </svg>
      <span>www.quorvana.com</span>
    </div>
    <svg class="footer-bands" viewBox="0 0 320 60" aria-hidden="true">
      <polygon points="0,22 90,22 70,60 0,60" fill="#4f8fb3"/>
      <polygon points="108,10 320,28 320,60 86,60" fill="#29a8e0"/>
    </svg>
  </section>

  <section class="card card-front">
    <div class="brand-name">quorvana</div>
    <div class="accent-bar"></div>
    <div class="name-plate">
      <div class="person">Dale<br>Fenwick</div>
      <div class="title">President</div>
    </div>
    <ul class="contact-list">
      <li>
        <svg class="icon" viewBox="0 0 20 20" aria-hidden="true">
          <rect width="20" height="20" rx="4" fill="#29a8e0"/>
          <path d="M6 4.5c.6-.4 1.2-.3 1.6.3l1 1.7c.3.5.2 1-.2 1.4l-.8.7c.6 1.3 1.5 2.3 2.8 2.9l.7-.8c.4-.4.9-.5 1.4-.2l1.7 1c.6.4.7 1 .3 1.6l-.7.9c-.5.6-1.3.8-2.1.5C8.9 13.5 6.5 11.1 5.5 8.3c-.3-.8-.1-1.6.5-2.1z" fill="#fff"/>
        </svg>
        <span>(800) 417-2964</span>
      </li>
      <li>
        <svg class="icon" viewBox="0 0 20 20" aria-hidden="true">
          <rect width="20" height="20" rx="4" fill="#29a8e0"/>
          <rect x="4" y="6" width="12" height="8.5" fill="none" stroke="#fff" stroke-width="1.3"/>
          <polyline points="4,6 10,11 16,6" fill="none" stroke="#fff" stroke-width="1.3"/>
        </svg>
        <span>sleep@quorvana.com</span>
      </li>
      <li>
        <svg class="icon" viewBox="0 0 20 20" aria-hidden="true">
          <rect width="20" height="20" rx="4" fill="#29a8e0"/>
          <circle cx="10" cy="10" r="6" fill="none" stroke="#fff" stroke-width="1.3"/>
          <ellipse cx="10" cy="10" rx="2.6" ry="6" fill="none" stroke="#fff" stroke-width="1.1"/>
          <line x1="4" y1="10" x2="16" y2="10" stroke="#fff" stroke-width="1.1"/>
        </svg>
        <span>www.quorvana.com</span>
      </li>
    </ul>
    <svg class="footer-bands" viewBox="0 0 320 60" aria-hidden="true">
      <polygon points="0,22 90,22 70,60 0,60" fill="#4f8fb3"/>
      <polygon points="108,10 320,28 320,60 86,60" fill="#29a8e0"/>
    </svg>
  </section>

</body>
</html>
```